Brill's Jewelers website (www.brillsjewelers-example.com)

We are in need of a web storefront for a retail Jewelry store.
www.brillsjewelers-example.com
https://www.facebook.com/Brills-Jewelers-Palm-Harbor-731450928814265/

Brill's Jewelers is located in Coral Gables, Florida. The store has been family owned and operated since 1958. Their focus customers are high-income families that care about quality over the brand name. They mostly sell fashion jewelry and diamonds up to 8 carats. We are looking for a simple minimalistic site that their customers can view their inventory and purchase items online.

Competitors websites:
https://www.tovinjewelers-example.com/
http://www.varelso-example.com/
http://craftedringshop-example.com/

Pages:
-Home (with message bulletin)
-Jewelry
We would be able to create the subpages ie Rings, Bracelets, Earrings, Necklaces, Estate, Watches, Men's, Children's
-Services
We would need sub pages ie Appraisals, Consignment, Repairs
-About us
-Contact

Target Market(s)

Local wealthy families

Coding

Coded - Design and coding required

Number of Pages Required

5+ page

Font styles to use
Serif

Requirements
Must have
• -An E-commerce site customers can buy jewelry online.
-An easy process internally to add new items to the site
-Colors are Black and White or Black and Gold
Nice to have
• I would like to stay away from face shots of random models in stock photos. I want the jewelry pieces as the focus, not models.

```html
<!DOCTYPE html>
<html lang="en">
<head>
<meta charset="utf-8">
<title>Brill's Jewelers</title>
<link href="https://fonts.googleapis.com/css2?family=Tinos:wght@400;700&family=Montserrat:wght@400;500&family=Poppins:wght@600&display=swap" rel="stylesheet">
<style>
:root{
  --gold:#d2b460;
  --gold-dark:#c19f45;
  --cream:#f3ead4;
  --cream-light:#f9f4e8;
  --ink:#111;
  --text:#444;
  --muted:#bbb;
  --white:#fff;
}
*{margin:0;padding:0;box-sizing:border-box}
html,body{width:1200px;height:5188px;overflow:hidden}
body{position:relative;background:var(--white);font-family:'Montserrat',sans-serif;color:var(--text)}
.abs{position:absolute}
.photo{position:absolute}
/* header */
.header{position:absolute;left:0;top:0;width:1200px;height:92px;background:var(--white)}
.brand{position:absolute;left:78px;top:28px;width:220px;font-family:'Tinos',serif;font-weight:400;font-size:30px;line-height:36px;color:var(--ink);white-space:nowrap}
.nav a{position:absolute;top:36px;font-size:15px;color:var(--ink);text-decoration:none}
.nav a.active{color:var(--gold)}
.nav a.active::after{content:"";position:absolute;left:0;right:0;top:24px;height:1px;background:var(--gold)}
/* hero */
.hero{position:absolute;left:0;top:92px;width:1200px;height:584px;background:radial-gradient(ellipse at 60% 40%,#6a5a48 0%,#3a3129 45%,#1d1915 100%)}
.hero-frame{position:absolute;left:188px;top:88px;width:824px;height:372px;border:1px solid var(--gold)}
.hero-dot{position:absolute;width:12px;height:12px;border-radius:50%;background:var(--gold)}
.hero-title{position:absolute;left:243px;top:120px;font-family:'Poppins',sans-serif;font-weight:600;font-size:38px;line-height:46px;color:var(--white)}
.hero-sub{position:absolute;left:248px;top:274px;font-size:23px;color:var(--gold)}
.btn{position:absolute;background:var(--gold);color:var(--white);font-family:'Tinos',serif;font-size:19px;letter-spacing:1px;display:flex;align-items:center;justify-content:center}
.arrow{position:absolute;width:46px;height:46px;border-radius:50%;background:rgba(210,180,96,.55);display:flex;align-items:center;justify-content:center}
.h2{position:absolute;left:0;width:1200px;text-align:center;font-family:'Tinos',serif;font-size:42px;color:var(--ink)}
.h2-sub{position:absolute;left:0;width:1200px;text-align:center;font-size:14px;color:var(--ink)}
.card-bg{position:absolute;background:linear-gradient(90deg,var(--cream) 0%,#f7f1e3 100%)}
.card-frame{position:absolute;border:1px solid var(--gold)}
.card-title{position:absolute;font-family:'Tinos',serif;font-size:26px;color:var(--ink)}
.card-text{position:absolute;font-size:14px;line-height:25px;color:var(--text)}
.services{position:absolute;left:0;top:2020px;width:1200px;height:428px;background:linear-gradient(90deg,#c9ad5d,#d9be72 50%,#c8ab5a)}
.svc{position:absolute;top:146px;width:190px;text-align:center;color:var(--white)}
.svc-icon{width:112px;height:112px;border-radius:50%;background:var(--white);margin:0 auto;display:flex;align-items:center;justify-content:center}
.svc-name{font-family:'Tinos',serif;font-size:22px;margin-top:20px}
.svc-text{font-size:14px;line-height:25px;margin-top:4px}
.tcard{position:absolute;top:3480px;width:392px;height:256px;background:var(--white);box-shadow:0 0 18px rgba(0,0,0,.07);padding:80px 20px 0 50px}
.tcard p{font-size:14px;line-height:27px}
.tcard .client{font-family:'Tinos',serif;font-size:17px;margin-top:18px}
.tcard .stars{color:var(--gold);font-size:13px;letter-spacing:4px;margin-left:22px}
.tcard.faded{opacity:.35}
.quote{position:absolute;top:3446px;width:72px;height:72px;border-radius:50%;background:var(--gold);color:var(--white);font-family:'Tinos',serif;font-size:64px;line-height:96px;text-align:center}
.lt-title{position:absolute;left:636px;top:3838px;font-family:'Tinos',serif;font-size:32px;line-height:42px;color:var(--ink);letter-spacing:1px}
.lt-item{position:absolute;left:636px;font-size:16px;color:var(--ink)}
.lt-item svg{vertical-align:middle;margin-right:24px}
.follow{position:absolute;left:0;top:4205px;width:1200px;height:195px;background:var(--cream-light)}
.news{position:absolute;left:0;top:4572px;width:1200px;height:274px;background:var(--gold)}
.news h3{position:absolute;left:0;width:1200px;top:90px;text-align:center;font-family:'Tinos',serif;font-weight:400;font-size:38px;color:var(--white)}
.news p{position:absolute;left:0;width:1200px;top:144px;text-align:center;font-size:15px;color:var(--white)}
.news-input{position:absolute;left:240px;top:192px;width:522px;height:62px;background:var(--white);font-size:13px;color:#555;padding:26px 24px}
.news-btn{position:absolute;left:762px;top:192px;width:198px;height:62px;border:1px solid var(--white);color:var(--white);font-family:'Tinos',serif;font-size:19px;display:flex;align-items:center;justify-content:center}
.f-head{position:absolute;top:4884px;font-family:'Tinos',serif;font-weight:700;font-size:17px;color:var(--ink);letter-spacing:1px}
.f-list{position:absolute;top:4934px;list-style:none;font-size:14px;line-height:29px;color:var(--text)}
.f-list li::before{content:"";display:inline-block;width:6px;height:6px;border-radius:50%;background:var(--gold);margin-right:14px;vertical-align:middle}
.f-contact{position:absolute;left:900px;font-size:14px;line-height:25px;color:var(--text)}
.f-ico{position:absolute;left:860px}
.copy{position:absolute;left:0;width:1200px;top:5150px;text-align:center;font-size:13px;color:var(--text)}
</style>
</head>
<body>

<header class="header">
  <div class="brand">Brill's Jewelers</div>
  <nav class="nav">
    <a class="active" style="left:614px">Home</a>
    <a style="left:693px">Jewelry</a>
    <a style="left:777px">Services</a>
    <a style="left:873px">About</a>
    <a style="left:944px">Contact Us</a>
  </nav>
  <svg class="abs" style="left:1044px;top:30px" width="34" height="32" viewBox="0 0 34 32"><path d="M3 6h5l4 14h14l3-10H10" fill="none" stroke="#111" stroke-width="2"/><circle cx="14" cy="25" r="2.2" fill="#111"/><circle cx="24" cy="25" r="2.2" fill="#111"/><circle cx="28" cy="6" r="6" fill="#d2b460"/></svg>
  <svg class="abs" style="left:1096px;top:34px" width="26" height="26" viewBox="0 0 26 26"><circle cx="13" cy="13" r="13" fill="#d2b460"/><circle cx="13" cy="10" r="4" fill="#fff"/><path d="M6 20c2-5 12-5 14 0" fill="#fff"/></svg>
</header>

<section class="hero">
  <div class="photo" role="img" aria-label="Rose gold beaded bracelets on a dark background" style="left:470px;top:60px;width:540px;height:500px;background:radial-gradient(ellipse at 55% 55%,#e2a98a 0%,#c98468 35%,rgba(120,80,60,0) 70%)"></div>
  <div class="hero-frame"></div>
  <div class="hero-dot" style="left:208px;top:126px"></div>
  <div class="hero-dot" style="left:650px;top:82px"></div>
  <div class="hero-title">YOUR HOMETOWN<br>JEWELERJUST GOT A<br>NEW HOME</div>
  <div class="hero-sub">VISIT US TODAY!</div>
  <div class="btn" style="left:248px;top:326px;width:166px;height:56px;font-size:20px">SHOP NOW</div>
  <div class="arrow" style="left:15px;top:280px"><svg width="12" height="18"><path d="M9 2L3 9l6 7" fill="none" stroke="#fff" stroke-width="1.5"/></svg></div>
  <div class="arrow" style="left:1138px;top:280px"><svg width="12" height="18"><path d="M3 2l6 7-6 7" fill="none" stroke="#fff" stroke-width="1.5"/></svg></div>
</section>

<h2 class="h2" style="top:746px">JEWELRY &amp; DIMONDS</h2>
<div class="h2-sub" style="top:803px">providing full jewelry services for you day in and day out.</div>

<div class="card-bg" style="left:142px;top:872px;width:360px;height:244px"></div>
<div class="card-frame" style="left:296px;top:906px;width:288px;height:188px"></div>
<div class="photo" role="img" aria-label="Diamond cross pendant" style="left:390px;top:904px;width:156px;height:262px;background:radial-gradient(ellipse,#e6e6e6 0%,#c8c8c8 30%,rgba(255,255,255,0) 65%)"></div>
<div class="card-title" style="left:172px;top:934px">Diamond</div>
<div class="card-text" style="left:174px;top:978px">Lorem Ipsum is simply<br>dummy text the print</div>

<div class="card-bg" style="left:696px;top:980px;width:362px;height:332px"></div>
<div class="card-frame" style="left:740px;top:1190px;width:274px;height:260px"></div>
<div class="photo" role="img" aria-label="Pearl drop earrings" style="left:760px;top:1220px;width:234px;height:200px;background:radial-gradient(circle at 30% 40%,#f2f2f2 0%,#dcdcdc 22%,rgba(255,255,255,0) 30%),radial-gradient(circle at 70% 60%,#f2f2f2 0%,#dcdcdc 22%,rgba(255,255,255,0) 30%)"></div>
<div class="card-title" style="left:736px;top:1020px">Pearls</div>
<div class="card-text" style="left:734px;top:1068px">Lorem Ipsum is simply dummy<br>text the print &nbsp;is simply &nbsp;text</div>

<div class="card-bg" style="left:302px;top:1196px;width:364px;height:246px"></div>
<div class="card-frame" style="left:212px;top:1228px;width:216px;height:204px"></div>
<div class="photo" role="img" aria-label="Yellow diamond halo ring" style="left:222px;top:1262px;width:196px;height:130px;background:radial-gradient(ellipse,#efe06a 0%,#d8d8d8 35%,rgba(255,255,255,0) 68%)"></div>
<div class="card-title" style="left:474px;top:1270px">Colored</div>
<div class="card-text" style="left:476px;top:1312px">Lorem Ipsum is simply<br>dummy text the print</div>

<div class="card-bg" style="left:142px;top:1514px;width:360px;height:348px"></div>
<div class="card-frame" style="left:402px;top:1556px;width:260px;height:256px"></div>
<div class="photo" role="img" aria-label="Diamond studded wristwatch" style="left:430px;top:1566px;width:236px;height:250px;background:radial-gradient(ellipse,#bcc7d6 0%,#a0a5ad 35%,rgba(255,255,255,0) 68%)"></div>
<div class="card-title" style="left:184px;top:1612px">Watches</div>
<div class="card-text" style="left:184px;top:1652px">Lorem Ipsum is simply<br>dummy text the print is<br>simply dummy text the<br>print</div>

<div class="card-bg" style="left:690px;top:1518px;width:362px;height:244px"></div>
<div class="card-frame" style="left:786px;top:1664px;width:232px;height:172px"></div>
<div class="photo" role="img" aria-label="Diamond engagement ring" style="left:806px;top:1700px;width:192px;height:100px;background:radial-gradient(ellipse,#e4e4e4 0%,#c6c6c6 30%,rgba(255,255,255,0) 65%)"></div>
<div class="card-title" style="left:730px;top:1550px">Estate</div>
<div class="card-text" style="left:730px;top:1586px">Lorem Ipsum is simply<br>dummy text the print</div>

<div class="btn" style="left:491px;top:1890px;width:218px;height:58px">EXLPORE MORE</div>

<section class="services">
  <h2 class="h2" style="top:62px;color:#fff">OUR SERVICES</h2>
  <div class="svc" style="left:212px"><div class="svc-icon"><svg width="60" height="60" viewBox="0 0 60 60" fill="none" stroke="#d2b460" stroke-width="2"><path d="M42 8a12 12 0 0 0-14 16L10 42a5 5 0 0 0 7 7l18-18a12 12 0 0 0 16-14l-7 7-6-2-2-6z"/></svg></div><div class="svc-name">Repairs</div><div class="svc-text">Lorem Ipsum is simply<br>text the print</div></div>
  <div class="svc" style="left:408px"><div class="svc-icon"><svg width="60" height="60" viewBox="0 0 60 60" fill="none" stroke="#d2b460" stroke-width="2"><path d="M30 16l4 9 10 1-7 7 2 10-9-5-9 5 2-10-7-7 10-1z"/><path d="M30 4v6M30 50v6M6 30h6M48 30h6M13 13l4 4M43 43l4 4M47 13l-4 4M17 43l-4 4"/></svg></div><div class="svc-name">Appraisals</div><div class="svc-text">Lorem Ipsum is simply<br>text the print</div></div>
  <div class="svc" style="left:605px"><div class="svc-icon"><svg width="66" height="60" viewBox="0 0 66 60" fill="none" stroke="#d2b460" stroke-width="2"><path d="M22 12h22l6 16H16zM8 34h24l4 14H4zM34 34h24l4 14H30z"/></svg></div><div class="svc-name">Buying Gold</div><div class="svc-text">Lorem Ipsum is simply<br>text the print</div></div>
  <div class="svc" style="left:801px"><div class="svc-icon"><svg width="60" height="60" viewBox="0 0 60 60" fill="none" stroke="#d2b460" stroke-width="2"><circle cx="30" cy="30" r="10"/><path d="M30 8v8M30 44v8M8 30h8M44 30h8M14 14l6 6M40 40l6 6M46 14l-6 6M20 40l-6 6"/><path d="M26 30l3 3 6-6"/></svg></div><div class="svc-name">Custom</div><div class="svc-text">Lorem Ipsum is simply<br>text the print</div></div>
</section>

<h2 class="h2" style="top:2506px">ABOUT BRILL'S</h2>
<div class="h2-sub" style="top:2565px">Providing full jewelry services for you day in and day out.</div>
<div class="photo" role="img" aria-label="Watchmaker repairing a watch beside a gold and steel wristwatch" style="left:270px;top:2616px;width:662px;height:374px;background:linear-gradient(90deg,#2a2a2a 0%,#8a8a8a 30%,#cfcfcf 45%,#3a3a3a 62%,#8a7443 78%,#e8e8e8 100%)"></div>
<p class="abs" style="left:290px;top:3022px;width:620px;text-align:center;font-size:14px;line-height:27px;color:#444">We are grateful for your patronage and loyalty over the past decades, helping you celebrate your special moments, and providing full jewelry services for you day in and day out. We are grateful for your patronage and loyalty over the past decades, helping you.</p>
<div class="btn" style="left:505px;top:3145px;width:189px;height:56px">LEARN MORE</div>
<div class="abs" style="left:326px;top:3262px;width:570px;height:3px;background:var(--gold)"></div>

<h2 class="h2" style="top:3330px">TESTIMONIALS</h2>
<div class="h2-sub" style="top:3386px;font-size:13px">What Our Client Say About Us !</div>
<div class="tcard faded" style="left:-30px;padding-left:52px"><p>Lorem Ipsum is simply dummy text of the printing and typesetting industry. Lorem Ipsum has been the indu stry.</p><div class="client">&#8211; &nbsp;Client Name</div><div class="stars">★★★★★</div></div>
<div class="tcard" style="left:404px"><p>Lorem Ipsum is simply dummy text of the printing and typesetting industry. Lorem Ipsum has been the indu stry.</p><div class="client">&#8211; &nbsp;Client Name</div><div class="stars">★★★★★</div></div>
<div class="tcard faded" style="left:832px;padding-left:50px"><p>Lorem Ipsum is simply dummy text of the printing and typesetting industry. Lorem Ipsum has been the indu str.</p><div class="client">&#8211; &nbsp;Client Name</div><div class="stars">★★★★★</div></div>
<div class="quote" style="left:6px;opacity:.4">&#8220;</div>
<div class="quote" style="left:442px">&#8220;</div>
<div class="quote" style="left:871px;opacity:.4">&#8220;</div>

<div class="photo" role="img" aria-label="Stacked silver and gold diamond bangles" style="left:180px;top:3800px;width:380px;height:380px;background:radial-gradient(ellipse at 40% 40%,#d6d6d6 0%,#c8c8c8 25%,rgba(255,255,255,0) 45%),radial-gradient(ellipse at 62% 62%,#e3c888 0%,#d6b66e 25%,rgba(255,255,255,0) 45%)"></div>
<svg class="abs" style="left:126px;top:3946px" width="16" height="34"><path d="M13 2L3 17l10 15" fill="none" stroke="#d2b460" stroke-width="1.5"/></svg>
<svg class="abs" style="left:558px;top:3946px" width="16" height="34"><path d="M3 2l10 15-10 15" fill="none" stroke="#d2b460" stroke-width="1.5"/></svg>
<div class="lt-title">LIFETIME SATIFACTION<br>GUARANTEED</div>
<div class="lt-item" style="top:3944px"><svg width="20" height="18"><path d="M2 9h14M10 3l6 6-6 6" fill="none" stroke="#d2b460" stroke-width="1.5"/></svg>45 Days Return</div>
<div class="lt-item" style="top:3986px"><svg width="20" height="18"><path d="M2 9h14M10 3l6 6-6 6" fill="none" stroke="#d2b460" stroke-width="1.5"/></svg>Lifetime Warranty</div>
<div class="lt-item" style="top:4028px"><svg width="20" height="18"><path d="M2 9h14M10 3l6 6-6 6" fill="none" stroke="#d2b460" stroke-width="1.5"/></svg>Lifetime Upgrade</div>
<div class="btn" style="left:636px;top:4078px;width:166px;height:56px">SHOP NOW</div>

<section class="follow">
  <h2 class="h2" style="top:70px">FOLLOW US ON</h2>
  <div class="abs" style="left:584px;top:136px;width:32px;height:32px;border-radius:8px;background:var(--gold)"></div>
</section>
<div class="photo" role="img" aria-label="Diamond rings on a dark surface" style="left:0;top:4400px;width:194px;height:172px;background:linear-gradient(135deg,#2e2e2e,#8c8c8c 55%,#3a3a3a)"></div>
<div class="photo" role="img" aria-label="Solitaire ring on red velvet" style="left:202px;top:4400px;width:194px;height:172px;background:linear-gradient(135deg,#f2f2f2 40%,#b42a2a 100%)"></div>
<div class="photo" role="img" aria-label="Ring with princess cut diamond" style="left:404px;top:4400px;width:194px;height:172px;background:linear-gradient(135deg,#cfcfcf,#8a8a8a 60%,#b0b0b0)"></div>
<div class="photo" role="img" aria-label="Model wearing a diamond necklace" style="left:606px;top:4400px;width:194px;height:172px;background:linear-gradient(135deg,#3b2a22,#a57a62 50%,#5a3e30)"></div>
<div class="photo" role="img" aria-label="Couple embracing" style="left:808px;top:4400px;width:194px;height:172px;background:linear-gradient(135deg,#e8dcd2,#b98c72 55%,#3d2a22)"></div>
<div class="photo" role="img" aria-label="Diamond necklace on white fabric" style="left:1010px;top:4400px;width:190px;height:172px;background:linear-gradient(135deg,#f4f2ee,#d6cfc4 55%,#ece8e0)"></div>

<section class="news">
  <h3>Signup For Newsletter !</h3>
  <p>Would you like to redeive our exclusive update for signup !</p>
  <div class="news-input">Enter Email *</div>
  <div class="news-btn">SUBSCRIBE</div>
</section>

<div class="brand" style="top:4938px">Brill's Jewelers</div>
<div class="abs" style="left:153px;top:5004px;width:48px;height:48px;border-radius:50%;background:var(--gold)"></div>

<div class="f-head" style="left:344px">SITEMAP</div>
<ul class="f-list" style="left:344px"><li>Home</li><li>Jewelry</li><li>Services</li><li>About</li><li>Contcat</li></ul>
<div class="f-head" style="left:610px">QUICK LINKS</div>
<ul class="f-list" style="left:610px"><li>Login/register</li><li>Order History</li><li>Shopping Cat</li><li>Whish List</li><li>Newsletter</li></ul>
<div class="f-head" style="left:864px">CONTACT INFO</div>
<svg class="f-ico" style="top:4938px" width="20" height="26"><path d="M10 2a7 7 0 0 1 7 7c0 6-7 14-7 14S3 15 3 9a7 7 0 0 1 7-7z" fill="none" stroke="#d2b460" stroke-width="1.6"/><circle cx="10" cy="9" r="2.5" fill="none" stroke="#d2b460" stroke-width="1.6"/></svg>
<div class="f-contact" style="top:4934px">418 Lantern Row, Coral<br>Gables, FL 33190</div>
<svg class="f-ico" style="top:5016px" width="20" height="16"><rect x="1" y="1" width="18" height="14" fill="#d2b460"/><path d="M1 2l9 7 9-7" fill="none" stroke="#fff" stroke-width="1.4"/></svg>
<div class="f-contact" style="top:5002px;width:240px;word-break:break-all">hello@brillsjewelers-example.com</div>
<svg class="f-ico" style="top:5062px" width="20" height="20"><path d="M4 2l4 1 1 4-2 2c1 2 3 4 5 5l2-2 4 1 1 4c-1 1-2 2-4 2C8 18 2 12 2 5c0-1 1-2 2-3z" fill="none" stroke="#d2b460" stroke-width="1.6"/></svg>
<div class="f-contact" style="top:5058px">(305)555-0187</div>

<div class="abs" style="left:80px;top:5128px;width:1040px;height:1px;background:#eee"></div>
<div class="copy">©BRILL'S - 2020 All rights reserved.</div>

</body>
</html>
```